Web Site Redesign

We operate a data centre facility specialing in colocation and Fibre optic connectivity (i.e. point to point fibre services and internet over fibre).

We have an existing site located at www.norvalex.example however this is very very tired and requires a redesign. We are looking for a fresh new design that will be appealing to potential customers.

The Company name is Norva eX and the primary corporate colour is bright red with secondary colours of white, grey and black. Specific bright red can be seen in attached company logo.

Website needs to be modern, clean and professional representing our premium colocation and fibre provider branding.

Our company slogan is : safe. secure. reliable

We will provide feedback regardless of the quality of the design to ensure a better outcome for all parties.

Please feel free to contact us if you have any questions.

# The designer can use placeholder images or feel free to use any/all or none of the attached images
# The designer can use sample filler text

Target Market(s)

Technical IT Professionals as well C level executives (i.e. CEO's, CIO).

Industry/Entity Type

Internet

Requirements
Must have
• clean design
Nice to have
• A sidebar with two sections. 1 for current promo and 1 for "Let us call you back/contact you"
Should not have
• Clutter

```html
<!DOCTYPE html>
<html lang="en">
<head>
<meta charset="utf-8">
<title>Norva eX — Safe. Secure. Reliable.</title>
<link rel="stylesheet" href="https://fonts.googleapis.com/css2?family=Arimo:ital,wght@0,400;0,700;1,400;1,700&family=Didact+Gothic&family=Questrial&display=swap">
<style>
  :root {
    --red: #d2112b;
    --red-deep: #a8061c;
    --red-light: #e8283f;
    --maroon: #4a2126;
    --maroon-deep: #331417;
    --ink: #111111;
    --grey-text: #5b5b5b;
    --grey-soft: #d6d6d6;
    --slogan: #dcdcdc;
    --paper: #ffffff;
    --brown-text: #6a4a4c;
  }
  * { box-sizing: border-box; margin: 0; padding: 0; }
  html, body { width: 1162px; height: 1200px; overflow: hidden; background: var(--paper); }
  .stage {
    position: relative; width: 1000px; height: 1033px;
    transform: scale(1.162); transform-origin: 0 0;
    font-family: "Arimo", Arial, sans-serif; color: var(--ink);
    background: linear-gradient(180deg, #f6f6f6 0, #ffffff 200px);
  }
  .abs { position: absolute; }

  /* header */
  .brand { left: 48px; top: 60px; display: flex; align-items: center; gap: 12px; }
  .brand-mark { width: 40px; height: 40px; background: var(--red); }
  .brand-name { font-family: "Questrial", sans-serif; font-size: 42px; color: var(--ink); line-height: 1; }
  .utility { right: 0; top: 0; display: flex; font-size: 13px; }
  .utility a { text-decoration: none; display: block; height: 36px; line-height: 42px; padding: 0 16px; color: var(--ink); }
  .utility .is-current { background: var(--red); color: #fff; font-weight: 700; border-bottom: 3px solid #5a0b14; line-height: 40px; }
  .slogan { left: 412px; top: 60px; font-family: "Questrial", sans-serif; font-size: 40px; color: var(--slogan); word-spacing: 36px; letter-spacing: 0.5px; }

  .main-nav {
    left: 226px; top: 141px; width: 774px; height: 51px;
    background: linear-gradient(180deg, var(--red-light), var(--red-deep));
    border-radius: 18px 0 0 0; clip-path: polygon(0 0, 100% 0, 100% 100%, 10px 100%, 4px 50%);
    display: flex; align-items: center; padding-left: 21px;
  }
  .main-nav a {
    color: #fff; text-decoration: none; font-weight: 700; font-size: 14px; letter-spacing: 0.3px;
    padding: 0 17px; line-height: 51px; border-right: 1px solid #7c0614;
    box-shadow: 1px 0 0 rgba(255,255,255,.15);
  }
  .main-nav a:last-child { border-right: 0; box-shadow: none; }

  /* hero */
  .hero { left: 15px; top: 207px; width: 973px; height: 314px; border: 4px solid #e4e4e4; border-radius: 10px; overflow: hidden; }
  .hero-photo { position: absolute; inset: 0; background: linear-gradient(100deg, #2c3036 0%, #5d6167 30%, #3a3d44 55%, #5a1a20 80%, #3b2a2c 100%); }
  .hero-title {
    position: absolute; left: 20px; top: 114px; width: 600px; text-align: center;
    font-weight: 700; font-style: italic; font-size: 27px; line-height: 36px; color: #fff;
    text-shadow: 0 0 3px #000, 2px 2px 3px #000;
  }
  .hero-circle { position: absolute; border-radius: 50%; border: 5px solid #fff; box-shadow: 0 0 4px rgba(0,0,0,.4); }
  .c-fibre { left: 620px; top: 19px; width: 168px; height: 168px; background: radial-gradient(circle at 40% 50%, #e08a3a, #6d6f73 60%, #3a3c40); }
  .c-server { left: 778px; top: 17px; width: 168px; height: 168px; background: radial-gradient(circle at 50% 40%, #8d8f94, #2b2c30 70%); }
  .c-office { left: 675px; top: 133px; width: 170px; height: 170px; background: radial-gradient(circle at 45% 40%, #e9e3d9, #b9b4ae 55%, #3b3b40); }

  /* content */
  .welcome { left: 25px; top: 538px; font-family: "Didact Gothic", sans-serif; font-size: 34px; color: var(--red); }
  .intro { left: 30px; top: 583px; width: 690px; font-size: 12px; line-height: 18px; color: var(--ink); }
  .intro p { margin-bottom: 18px; }

  /* sidebar */
  .promo { left: 740px; width: 247px; height: 179px; border-radius: 10px; overflow: hidden; background: #fff; box-shadow: 0 0 4px rgba(0,0,0,.2); }
  .promo-partner { top: 534px; }
  .promo-contact { top: 732px; }
  .promo-head { position: absolute; left: 0; top: 0; width: 247px; height: 118px; }
  .promo-copy { position: absolute; left: 0; width: 247px; text-align: center; font-style: italic; color: #fff; }
  .promo-partner .promo-copy { top: 13px; font-size: 17px; line-height: 22px; }
  .promo-contact .promo-copy { top: 18px; font-family: "Arimo", sans-serif; font-size: 20px; line-height: 30px; }
  .partner-badge { position: absolute; left: 66px; top: 125px; width: 116px; height: 44px; border-radius: 4px; background: #efe4e6; }
  .promo-callback { position: absolute; left: 0; top: 102px; width: 247px; text-align: center; font-size: 15.5px; line-height: 20px; color: var(--brown-text); }

  /* footer */
  .site-footer {
    left: 20px; top: 928px; width: 968px; height: 50px; border-radius: 12px;
    background: linear-gradient(180deg, var(--maroon), var(--maroon-deep));
    display: flex; align-items: center; justify-content: space-between; padding: 0 27px 0 29px; font-size: 11px;
  }
  .copyright { color: #7d5a5d; }
  .footer-nav { display: flex; gap: 16px; }
  .footer-nav a { color: #d9c6c8; text-decoration: none; }
</style>
</head>
<body>
<div class="stage">
  <header>
    <div class="abs brand"><span class="brand-mark"></span><span class="brand-name">Norva eX</span></div>
    <nav class="abs utility"><a class="is-current" href="#">Home</a><a href="#">Contact Us</a></nav>
    <div class="abs slogan">Safe. Secure. Reliable.</div>
    <nav class="abs main-nav">
      <a href="#">ABOUT US</a><a href="#">FACILITIES</a><a href="#">BUSINESS CONTINUITY</a><a href="#">SERVICES</a><a href="#">PARTNERS</a><a href="#">WEBMAIL</a>
    </nav>
  </header>

  <section class="abs hero">
    <div class="hero-photo" role="img" aria-label="Rows of server racks in a data centre"></div>
    <h1 class="hero-title">We are one of leading providers of<br>Data Connectivity and Telecommunications<br>Services for business.</h1>
    <div class="hero-circle c-fibre" role="img" aria-label="Close-up of orange fibre optic patch cables"></div>
    <div class="hero-circle c-server" role="img" aria-label="Rack-mounted server hardware"></div>
    <div class="hero-circle c-office" role="img" aria-label="Technician working on a laptop"></div>
  </section>

  <h2 class="abs welcome">Welcome to Norva eX</h2>
  <div class="abs intro">
    <p>A world class data centre in the safest place on Earth.</p>
    <p>With a centrally located data centre in the heart of the Norvale CBD Norva eX is excellently positioned to assist with your critical IT requirements.</p>
    <p>The CBD facility features overlapping power grids, redundant power supplies and comprehensively maintained infrastructure, providing excellent levels of protection for your critical IT equipment. The State's newest and most technologically advanced data centre is also now open in Eastmere, a convenient 5.5 km's from the CBD providing a perfect location for either production sites, or DR infrastructure.</p>
    <p>From Government departments to large corporations to SME's, Norva eX is the ideal company to assist with your colocation requirements. With warm racks already provisioned, you can begin using the data centre almost immediately.</p>
    <p>Call us today to see how we can help meet your needs.</p>
  </div>

  <aside>
    <div class="abs promo promo-partner">
      <svg class="promo-head" viewBox="0 0 247 118" aria-hidden="true">
        <defs><linearGradient id="partnerRed" x1="0" y1="0" x2="0" y2="1"><stop offset="0" stop-color="#a8061c"/><stop offset="1" stop-color="#e8283f"/></linearGradient></defs>
        <path d="M0 0H247V95Q124 128 0 105Z" fill="url(#partnerRed)"/>
      </svg>
      <p class="promo-copy">Norva eX partners with<br>Australia's leading<br>providers of IT solutions<br>and infrastructure.</p>
      <div class="partner-badge" role="img" aria-label="Partner badge"></div>
    </div>
    <div class="abs promo promo-contact">
      <svg class="promo-head" viewBox="0 0 247 118" aria-hidden="true">
        <defs><linearGradient id="contactMaroon" x1="0" y1="0" x2="0" y2="1"><stop offset="0" stop-color="#3a1518"/><stop offset="1" stop-color="#5a2a2e"/></linearGradient></defs>
        <path d="M0 0H247V88Q130 110 0 97Z" fill="url(#contactMaroon)"/>
      </svg>
      <p class="promo-copy">Norvale's Safe, Secure &amp;<br>Reliable Data Centre</p>
      <p class="promo-callback">Talk to us<br>about designing a solution<br>to meet your needs.</p>
    </div>
  </aside>

  <footer class="abs site-footer">
    <span class="copyright">Copyright © 2010. All right reserved.</span>
    <nav class="footer-nav"><a href="#">Home</a><a href="#">About Us</a><a href="#">Facilities</a><a href="#">Business Continuity</a><a href="#">Services</a><a href="#">Partners</a><a href="#">Webmail</a><a href="#">Contact</a></nav>
  </footer>
</div>
</body>
</html>
```